Oil and Gas Industry training School Needs a Web Design

We need a web design for a new company based in Northern British Columbia Canada called "SKILLSPAN Industry Training Inc." Is a training facility that specializes in different aspects of Pipeline Construction training. We also offer compliance courses for Oil and Gas Industry. We would like to see designs that us the colours in our logo.

Target Market(s)

Is Men and women between 18-60 that want to work in the oil and gas industry

Industry/Entity Type

School

Number of Pages Required

5+ page

Font styles to use
Sans Serif

Colors
f37022
000000
333333
ffffff
848484
7f7f7f
c8c8c8
f68d4d
fee3d4

Requirements
Must have
• a easy back end for editing content! and adding additional pages if necessary.

```html
<!DOCTYPE html>
<html lang="en">
<head>
<meta charset="utf-8">
<title>SKILLSPAN Industry Training Inc.</title>
<link href="https://fonts.googleapis.com/css2?family=Open+Sans:wght@400;600;700&display=swap" rel="stylesheet">
<style>
:root{
  --orange:#f37022;
  --orange-light:#f68d4d;
  --orange-pale:#fee3d4;
  --black:#000000;
  --dark:#231f20;
  --charcoal:#333333;
  --grey:#848484;
  --grey-mid:#7f7f7f;
  --grey-line:#c8c8c8;
  --panel:#f0f0f0;
  --white:#ffffff;
  --social:#1a8fd6;
}
*{box-sizing:border-box;margin:0;padding:0}
html,body{width:1024px;height:1200px;overflow:hidden;background:var(--white)}
body{font-family:"Open Sans",Arial,sans-serif;color:var(--charcoal);position:relative}
.abs{position:absolute}

/* header */
.brand{left:42px;top:22px;display:flex;align-items:center;gap:18px}
.brand-mark{width:82px;height:82px;border-radius:50%;background:var(--orange)}
.brand-name{font-weight:700;color:#555;line-height:1}
.brand-name .word{font-size:40px;letter-spacing:.5px;display:block}
.brand-name .sub{font-size:15px;letter-spacing:1.5px;display:block;margin-top:8px;padding-left:8px}
.tagline{left:571px;top:21px;font-size:13px;font-weight:600;color:var(--orange)}
.account{left:861px;top:20px;font-size:14px;font-weight:600;color:var(--grey)}
.search{left:567px;top:54px;width:265px;height:40px;background:#f0f0f0;display:flex;justify-content:flex-end}
.search-btn{width:40px;height:40px;background:var(--grey-line);display:flex;align-items:center;justify-content:center}
.social{top:54px;width:40px;height:40px;background:var(--social)}

.nav{left:42px;top:124px;width:940px;height:52px;border-top:1px solid #e4e4e4;border-bottom:1px solid #e4e4e4}
.nav a{position:absolute;top:16px;font-size:14px;font-weight:700;color:#444;text-decoration:none;text-transform:uppercase}
.nav a.active{color:var(--orange)}

/* hero */
.hero{left:42px;top:201px;width:946px;height:378px;background:var(--dark)}
.hero-crumbs{left:38px;top:36px;font-size:13px;color:#e6e0c8}
.hero-title{left:33px;top:74px;font-size:45px;font-weight:600;color:var(--white)}
.hero-text{left:38px;top:129px;width:360px;font-size:19px;font-weight:600;line-height:27px;color:var(--white)}
.btn-orange{left:35px;top:226px;width:210px;height:39px;background:var(--orange);color:var(--white);font-size:17px;font-weight:700;display:flex;align-items:center;justify-content:center}
.dots{left:35px;top:331px;display:flex;gap:14px}
.dots span{width:17px;height:17px;border-radius:50%;background:var(--white)}
.dots span.on{background:#9a9a9a}
.hero-photo{left:440px;top:0;width:506px;height:378px;background:linear-gradient(160deg,#e8e6e0 0%,#b9b3a8 45%,#5d5a60 100%)}

/* section headers */
.block-head{height:59px;background:var(--dark);color:var(--white);font-size:16px;font-weight:700;text-transform:uppercase;display:flex;align-items:center;justify-content:center}
.vline{top:604px;width:1px;height:596px;background:#e4e4e4}
.hline{height:1px;background:#e0e0e0}

/* left column */
.book{left:42px;top:604px;width:300px;justify-content:flex-start;padding-left:22px}
.book-arrow{position:absolute;right:0;top:0;width:58px;height:59px;border-left:2px solid var(--white);display:flex;align-items:center;justify-content:center}
.courses-head{left:42px;top:704px;width:300px}
.courses{left:42px;top:763px;width:300px;height:407px;background:var(--panel);padding:0 20px}
.courses .hint{font-size:14px;color:var(--grey);padding:16px 0 16px}
.courses li{list-style:none;height:38px;border-top:1px solid var(--grey-line);display:flex;align-items:center;justify-content:space-between;padding:0 8px;font-size:15px;font-weight:700;color:var(--orange)}

/* middle column */
.about-head{left:382px;top:604px;width:340px}
.about{left:384px;top:676px;width:336px}
.about h2{font-size:15px;font-weight:700;color:var(--grey-mid);line-height:19px;margin-bottom:18px}
.about p{font-size:15px;color:var(--grey);line-height:19px;margin-bottom:19px}
.about .more{font-size:16px;font-weight:700;color:var(--orange);margin-top:30px}
.clients-head{left:382px;top:1022px;width:340px}
.client-card{left:452px;top:1100px;width:200px;height:110px;border:1px solid #ddd;border-radius:4px;box-shadow:0 1px 4px rgba(0,0,0,.2);display:flex;align-items:center;justify-content:center;gap:10px}
.client-card .dot{width:22px;height:22px;background:var(--charcoal)}
.client-card .name{font-size:30px;font-weight:700;color:var(--charcoal)}

/* right column */
.news-head{left:762px;top:604px;width:220px}
.news-item{left:762px;width:220px}
.news-item h3{font-size:15px;font-weight:700;color:var(--grey-mid);line-height:19px}
.news-item time{display:block;font-size:11px;color:var(--grey);margin-top:4px}
.connect-head{left:762px;top:863px;width:220px}
.widget{left:770px;top:929px;width:212px}
.widget-top{display:flex;gap:10px;align-items:flex-start}
.widget-mark{width:40px;height:40px;border-radius:50%;background:var(--orange)}
.widget-name{font-size:13px;color:#2a55b8}
.like{display:inline-block;margin-top:4px;background:#4a66a8;color:var(--white);font-size:11px;font-weight:700;padding:1px 6px}
.widget-count{font-size:11px;color:var(--black);margin-top:14px;padding-top:8px;border-top:1px solid #ddd}
.widget-count span{color:#2a55b8}
.avatars{display:grid;grid-template-columns:repeat(4,50px);gap:4px;margin-top:8px}
.avatars div{width:50px;height:50px;background:linear-gradient(135deg,#b9a08a,#5a4a44)}
.widget-foot{font-size:9px;color:var(--grey);margin-top:14px;padding-top:6px;border-top:1px solid #ddd}
.next-head{left:762px;top:1192px;width:220px;height:20px;background:var(--dark)}
</style>
</head>
<body>

<header>
  <div class="abs brand">
    <div class="brand-mark" aria-hidden="true"></div>
    <div class="brand-name"><span class="word">SKILLSPAN</span><span class="sub">INDUSTRY TRAINING INC.</span></div>
  </div>
  <div class="abs tagline">Growing people. Enhancing performance.</div>
  <div class="abs account">Login&nbsp; /&nbsp; Register</div>
  <div class="abs search">
    <div class="search-btn">
      <svg width="20" height="20" viewBox="0 0 20 20"><circle cx="8" cy="8" r="6" fill="none" stroke="#fff" stroke-width="3"/><line x1="12.5" y1="12.5" x2="18" y2="18" stroke="#fff" stroke-width="3.5" stroke-linecap="round"/></svg>
    </div>
  </div>
  <div class="abs social" style="left:842px" aria-label="Social link one"></div>
  <div class="abs social" style="left:892px" aria-label="Social link two"></div>
  <div class="abs social" style="left:942px;background:#1770b0" aria-label="Social link three"></div>

  <nav class="abs nav">
    <a class="active" style="left:24px">Home</a>
    <a style="left:118px">About us</a>
    <a style="left:241px">FAQs</a>
    <a style="left:329px">Open training courses</a>
    <a style="left:562px">In-house training</a>
    <a style="left:757px">News</a>
    <a style="left:850px">Contact</a>
  </nav>
</header>

<section class="abs hero">
  <div class="abs hero-crumbs">Business and Commercial / Financial / Management</div>
  <h1 class="abs hero-title">Global reach</h1>
  <p class="abs hero-text">Delivering worldwide training programmes for people in Oil &amp; Gas and Energy.</p>
  <div class="abs btn-orange">Book a course now</div>
  <div class="abs dots"><span></span><span class="on"></span><span></span><span></span><span></span></div>
  <div class="abs hero-photo" role="img" aria-label="Photo of a group of course participants in a training room"></div>
</section>

<div class="abs vline" style="left:362px"></div>
<div class="abs vline" style="left:742px"></div>

<!-- left column -->
<div class="abs block-head book">Book a course now
  <div class="book-arrow"><svg width="22" height="22" viewBox="0 0 22 22"><polyline points="3,3 19,11 3,19" fill="none" stroke="#fff" stroke-width="3"/></svg></div>
</div>
<div class="abs hline" style="left:42px;top:683px;width:300px"></div>
<div class="abs block-head courses-head">Open training course</div>
<div class="abs courses">
  <div class="hint">Search course by location</div>
  <ul>
    <li>Aberdeen<span>&gt;</span></li>
    <li>Doha<span>&gt;</span></li>
    <li>Dubai<span>&gt;</span></li>
    <li>Kuala Lumpur<span>&gt;</span></li>
    <li>London<span>&gt;</span></li>
    <li>Perth WA<span>&gt;</span></li>
    <li>Dar es Salaam<span>&gt;</span></li>
    <li>Rio de Janeiro<span>&gt;</span></li>
    <li>Nairobi<span>&gt;</span></li>
  </ul>
</div>
<div class="abs hline" style="left:42px;top:1190px;width:300px"></div>

<!-- middle column -->
<div class="abs block-head about-head">About us</div>
<div class="abs about">
  <h2>Financial, commercial and management training courses for the oil &amp; gas industry</h2>
  <p>Since 1992, we has delivered thou sands of training courses in over 70 countries designed to help oil and gas industry personnel to enhance their skills - and their performance in the workplace.</p>
  <p>Over the years, we has built up an impressive range of practical training courses on key financial, commercial and management topics, available on both an open and an in-house basis.</p>
  <div class="more">Find out more about us</div>
</div>
<div class="abs hline" style="left:382px;top:1000px;width:340px"></div>
<div class="abs block-head clients-head">Our global client base</div>
<div class="abs client-card"><span class="dot"></span><span class="name">NORVIK</span></div>

<!-- right column -->
<div class="abs block-head news-head">Our news</div>
<article class="abs news-item" style="top:678px">
  <h3>Industry Knowledge and Expertise</h3>
  <time>4th of August 2014</time>
</article>
<div class="abs hline" style="left:762px;top:752px;width:220px"></div>
<article class="abs news-item" style="top:762px">
  <h3>Industry View: Training gone global</h3>
  <time style="margin-top:8px">14th of July 2014</time>
</article>
<div class="abs hline" style="left:762px;top:837px;width:220px"></div>
<div class="abs block-head connect-head">Stay connected</div>
<div class="abs widget">
  <div class="widget-top">
    <div class="widget-mark" aria-hidden="true"></div>
    <div>
      <div class="widget-name">Skillspan_Training</div>
      <div class="like">Like</div>
    </div>
  </div>
  <div class="widget-count">465 people like <span>Skillspan Training</span></div>
  <div class="avatars" role="img" aria-label="Profile photos of followers">
    <div></div><div></div><div></div><div></div>
    <div></div><div></div><div></div><div></div>
  </div>
  <div class="widget-foot">Social media plugin</div>
</div>
<div class="abs next-head"></div>

</body>
</html>
```